592RidgeWatt Korvath TR-2300 2016 Van Wrap

I own a renewable energy company focused on solar panel sales an installation. I need a van wrap created for my Korvath TR-2300 2016 Van. May add additional vehicles to the fleet. I would like the design to be colorful and eye catching but professional. I would like solar panels to be a large part of the design. The design should fill the van, but not make it over crowded. Include slogan across the back door stating, "Tired of high electric bills? Solar energy is the solution!"

Target Market(s)

Home owner and anyone interesting in renewable energy

Requirements
Must have
• I want my number included (1-833-555-0187) as well as my website url (http://www.592ridgewatt.com). The logo attached below also needs to be implemented. I want the colors of the wrap based off of the colors used in the logo.
Professional appearance is needed. Include slogan across the back door stating, "Tired of high electric bills? Solar energy is the solution!"
Nice to have
• Solar panels
Sun
Slogan about solar maybe
Should not have
• Profanities
Inappropriate pictures
Unprofessional appearance.

```html
<!DOCTYPE html>
<html lang="en">
<head>
<meta charset="utf-8">
<title>592RidgeWatt Van Wrap</title>
<link href="https://fonts.googleapis.com/css2?family=Montserrat:wght@500;600;800&display=swap" rel="stylesheet">
<style>
  :root {
    --wrap-blue: #2a7dc4;
    --wrap-orange: #e38a2a;
    --wrap-white: #eef0f2;
    --glass: #b9bcc0;
    --trim-dark: #1f2124;
    --seam: #c9ccd0;
    --arch: #2c2f33;
    --bumper: #a9adb2;
    --shadow: #d9dadc;
    --page: #ffffff;
  }
  html, body {
    margin: 0;
    padding: 0;
    width: 1200px;
    height: 797px;
    overflow: hidden;
    background: var(--page);
  }
  .wrap-canvas {
    display: block;
    width: 1200px;
    height: 797px;
  }
  .body-blue { fill: var(--wrap-blue); }
  .body-white { fill: var(--wrap-white); }
  .stripe-orange { fill: var(--wrap-orange); }
  .glass { fill: var(--glass); }
  .trim { fill: var(--trim-dark); }
  .arch { fill: var(--arch); }
  .seam { fill: none; stroke: var(--seam); stroke-width: 3; }
  .seam-dark { fill: none; stroke: #1a5d97; stroke-width: 3; opacity: 0.5; }
  .ground-shadow { fill: var(--shadow); }
  .bumper { fill: var(--bumper); }
  .lamp-front { fill: #e6e6e6; }
  .lamp-signal { fill: var(--wrap-orange); }
  .lamp-rear { fill: #8e1a1f; }
  .wheel-area { fill: var(--trim-dark); }
  .hub-area { fill: #a3a7ac; }
  .hub-center { fill: #7d8186; }
  .phone {
    font-family: "Montserrat", sans-serif;
    font-weight: 600;
    font-size: 37px;
    fill: var(--wrap-white);
  }
  .brand-name {
    font-family: "Montserrat", sans-serif;
    font-weight: 600;
    font-size: 96px;
    fill: var(--wrap-blue);
  }
  .brand-mark { fill: var(--wrap-orange); }
  .site-url {
    font-family: "Montserrat", sans-serif;
    font-weight: 600;
    font-size: 48px;
    fill: var(--wrap-blue);
  }
  .slogan-question {
    font-family: "Montserrat", sans-serif;
    font-weight: 800;
    font-size: 52px;
    fill: var(--wrap-white);
  }
  .slogan-answer {
    font-family: "Montserrat", sans-serif;
    font-weight: 800;
    font-size: 46px;
    fill: var(--wrap-orange);
  }
</style>
</head>
<body>
<svg class="wrap-canvas" viewBox="0 0 2100 1397" xmlns="http://www.w3.org/2000/svg">
  <defs>
    <clipPath id="van-body-clip">
      <path d="M60,930 L52,800 L70,680 L100,620 Q130,580 300,560 L480,548 L560,530 L720,360 Q740,350 800,348 L1930,330 Q1965,332 1972,360 L1992,500 L2000,900 L60,930 Z"/>
    </clipPath>
  </defs>

  <ellipse class="ground-shadow" cx="1050" cy="1000" rx="960" ry="40"/>

  <g class="van-body" clip-path="url(#van-body-clip)">
    <rect class="body-blue" x="0" y="300" width="2100" height="700"/>
    <path class="body-white" d="M620,500 Q760,700 835,960 L1620,960 L1540,740 L1290,320 L700,320 Z"/>
    <path class="stripe-orange" d="M582,512 Q725,705 798,960 L835,960 Q760,700 620,500 Z"/>
    <path class="stripe-orange" d="M1280,320 L1345,320 L1580,740 L1620,960 L1575,960 L1535,745 Z"/>
    <path class="arch" d="M200,930 Q210,740 370,740 Q530,740 545,930 Z"/>
    <path class="arch" d="M1470,930 Q1480,735 1630,735 Q1780,735 1795,930 Z"/>
  </g>

  <g class="panel-seams">
    <path class="seam" d="M975,365 L975,910"/>
    <path class="seam" d="M1440,335 L1440,920"/>
    <path class="seam" d="M1042,395 Q1042,378 1062,378 L1430,378"/>
    <path class="seam-dark" d="M1440,335 L1440,920 M1925,335 L1945,900"/>
    <path class="seam-dark" d="M1440,378 L1895,375 Q1912,378 1912,398 L1912,525 Q1912,540 1895,540 L1440,540"/>
    <rect class="seam" x="1465" y="688" width="62" height="48" rx="8"/>
    <path class="seam-dark" d="M565,575 L570,910"/>
  </g>

  <path class="trim" d="M640,530 L715,385 L945,385 L945,585 Q920,590 770,595 Z"/>
  <path class="glass" d="M665,528 L728,403 L932,400 L932,572 L770,580 Z"/>
  <path class="trim" d="M565,540 L700,375 L722,378 L600,530 Z"/>
  <path class="trim" d="M615,545 Q615,505 655,503 L675,505 L675,590 L630,595 Q615,590 615,570 Z"/>
  <rect class="trim" x="865" y="632" width="75" height="12" rx="6"/>
  <path class="trim" d="M560,935 L1440,935 L1440,945 L560,945 Z" opacity="0.7"/>

  <path class="bumper" d="M50,805 L200,815 L200,935 L60,930 Z"/>
  <path class="lamp-front" d="M85,672 L170,670 L160,745 L85,748 Z"/>
  <path class="lamp-signal" d="M140,675 L170,672 L165,695 L138,697 Z"/>
  <path class="lamp-rear" d="M1968,610 L2005,605 L2005,740 L1968,738 Z"/>
  <path class="bumper" d="M1990,825 L2045,830 L2045,895 L1990,900 Z"/>

  <g role="img" aria-label="Front wheel and tyre">
    <circle class="wheel-area" cx="370" cy="920" r="135"/>
    <circle class="hub-area" cx="370" cy="920" r="82"/>
    <circle class="hub-center" cx="370" cy="920" r="32"/>
  </g>
  <g role="img" aria-label="Rear wheel and tyre">
    <circle class="wheel-area" cx="1630" cy="925" r="135"/>
    <circle class="hub-area" cx="1630" cy="925" r="82"/>
    <circle class="hub-center" cx="1630" cy="925" r="32"/>
  </g>

  <text class="phone" x="245" y="677">1-833-555-0187</text>

  <g class="brand-lockup">
    <circle class="brand-mark" cx="1200" cy="530" r="130"/>
    <text class="brand-name" x="1190" y="762" text-anchor="middle">592RidgeWatt</text>
  </g>

  <text class="site-url" x="1133" y="857" text-anchor="middle">www.592ridgewatt.com</text>

  <text class="slogan-question" text-anchor="middle">
    <tspan x="1680" y="434">Tired Of High</tspan>
    <tspan x="1680" y="499">Electric Bills?</tspan>
  </text>
  <text class="slogan-answer" text-anchor="middle">
    <tspan x="1748" y="595">Solar Energy Is</tspan>
    <tspan x="1748" y="653">The Solution!</tspan>
  </text>
</svg>
</body>
</html>
```